Modernize Police Fraternity Website

We're in search of a web developer to rejuvenate the digital presence of our co-ed fraternity at Marwick Vale State, which is dedicated to supporting students pursuing careers in criminal justice and law enforcement. We aim for a modern, minimalist website that's both user-friendly and simple to maintain. Key features will include an inviting landing page, an easy-to-use contact form, and a secure online store for handling memberships, donations, and sales of items like t-shirts. While we're eager to retain as much of our existing content as possible, we're also open to thoughtful content adjustments to elevate our design. For a glimpse of our current website and to understand our mission, please visit brenfieldcircle.org.

Target Market(s)

Students

Coding

Coded - Design and coding required

Number of Pages Required

4 page

Font styles to use
Serif

Colors

Designer to choose colors to be used in the design.

Requirements
Must have
• Landing page, contact us, shop
Nice to have
• membership tracking

```html
<!DOCTYPE html>
<html lang="en">
<head>
<meta charset="utf-8">
<title>Brenfield Circle Fraternity</title>
<link href="https://fonts.googleapis.com/css2?family=Marcellus&family=Arimo:wght@400;700&display=swap" rel="stylesheet">
<style>
:root{
  --red:#8a1c12;
  --red-deep:#6e1008;
  --red-soft:#b84a3c;
  --ink:#222;
  --muted:#444;
  --grey-bg:#f2f2f2;
  --blush:#f1e6e5;
  --footer:#2b2b2b;
  --white:#fff;
}
*{margin:0;padding:0;box-sizing:border-box}
html,body{width:1200px;height:4478px;overflow:hidden}
body{position:relative;background:var(--white);font-family:'Arimo',Arial,sans-serif;color:var(--ink)}
.serif{font-family:'Marcellus',Georgia,serif}
section,header,footer{position:absolute;left:0;width:1200px}
.abs{position:absolute}
.btn{position:absolute;border:2px solid var(--red);color:var(--red);font-family:'Marcellus',Georgia,serif;font-size:14px;letter-spacing:.5px;display:flex;align-items:center;justify-content:center;background:transparent}
.btn.light{border-color:var(--white);color:var(--white)}
.rule{position:absolute;height:3px;background:var(--red);width:88px}
.title{position:absolute;font-family:'Marcellus',Georgia,serif;font-size:33px;color:var(--ink);letter-spacing:.5px}

/* header */
.site-header{top:0;height:139px;background:var(--white);border-top:5px solid var(--red-deep)}
.nav a{position:absolute;top:62px;font-size:14px;color:var(--ink);text-decoration:none}
.brand{position:absolute;left:540px;top:18px;width:120px;height:105px;display:flex;flex-direction:column;align-items:center;justify-content:center;gap:6px}
.brand .dot{width:34px;height:34px;border-radius:50%;background:var(--red)}
.brand span{font-family:'Marcellus',Georgia,serif;font-size:14px;color:var(--red)}
.mail-badge{position:absolute;left:892px;top:48px;width:50px;height:50px;border-radius:50%;background:var(--red)}

/* hero */
.hero{top:139px;height:610px}
.hero-photo{position:absolute;left:0;top:0;width:1200px;height:602px;border-bottom-right-radius:260px 230px;background:linear-gradient(90deg,var(--red-deep) 0%,#8f2a1c 40%,#c9a9a0 70%,#e6d7d2 100%);box-shadow:8px 8px 0 #ead6d3}
.hero h2{position:absolute;left:111px;top:140px;font-family:'Marcellus',Georgia,serif;color:var(--white);font-weight:400}
.hero .kicker{font-size:36px;top:138px}
.hero .name{font-size:66px;line-height:70px;top:205px}
.hero .arrow{position:absolute;top:278px}

/* about */
.about{top:749px;height:621px}
.about-mark{position:absolute;left:128px;top:84px;width:377px;height:455px;display:flex;flex-direction:column;align-items:center;justify-content:center;gap:18px}
.about-mark .dot{width:120px;height:120px;border-radius:50%;background:var(--red)}
.about-mark span{font-family:'Marcellus',Georgia,serif;font-size:34px;color:var(--red)}
.about p{position:absolute;left:613px;top:196px;width:475px;font-size:12.5px;line-height:25px;color:var(--muted);text-align:justify}

/* features */
.features{top:1370px;height:558px}
.features-bg{position:absolute;inset:0;background:radial-gradient(ellipse at 70% 30%,#a8463a 0%,var(--red) 45%,var(--red-deep) 100%)}
.feature{position:absolute;top:197px;width:230px;text-align:center;color:var(--white)}
.feature .disc{width:143px;height:143px;border-radius:50%;background:var(--white);margin:0 auto;display:flex;align-items:center;justify-content:center}
.feature h3{font-family:'Marcellus',Georgia,serif;font-weight:400;font-size:18px;margin-top:32px}
.feature p{font-size:12px;line-height:22px;margin-top:14px}

/* social */
.social{top:1928px;height:577px}
.social-dot{position:absolute;top:177px;width:87px;height:87px;border-radius:50%;background:var(--white);box-shadow:0 3px 12px rgba(0,0,0,.12)}
.social h4{position:absolute;left:111px;top:302px;font-family:'Marcellus',Georgia,serif;font-weight:400;font-size:21px;color:var(--red)}
.social p{position:absolute;left:111px;top:356px;width:480px;font-size:14px;line-height:28px;color:var(--muted)}
.group-photo{position:absolute;left:667px;top:87px;width:422px;height:403px;background:linear-gradient(160deg,#b79d8c 0%,#8e8a8e 50%,#6d5a5a 100%)}

/* memberships */
.members{top:2505px;height:428px;background:var(--grey-bg)}
.members-photo{position:absolute;left:0;top:0;width:560px;height:428px;background:linear-gradient(90deg,#6a2a2a 0%,#7a3434 55%,var(--grey-bg) 100%)}
.members p{position:absolute;left:599px;top:165px;width:420px;font-size:14px;line-height:26px;color:var(--muted)}

/* shop */
.shop{top:2933px;height:607px}
.product{position:absolute;top:172px;width:232px}
.product .shot{height:177px;background:var(--white);box-shadow:0 2px 10px rgba(0,0,0,.08);display:flex;align-items:center;justify-content:center}
.product .tee{width:110px;height:130px;border-radius:10px}
.product h5{font-family:'Marcellus',Georgia,serif;font-weight:400;font-size:17px;margin-top:26px;color:var(--ink)}
.product .price{font-family:'Marcellus',Georgia,serif;font-size:20px;color:var(--red);margin-top:16px}
.product .stars{font-size:13px;color:var(--red);letter-spacing:1px;margin-top:6px}
.product .btn{position:relative;width:102px;height:44px;margin-top:14px}

/* contact */
.contact{top:3540px;height:550px;background:var(--blush)}
.field{position:absolute;height:50px;background:var(--white);font-size:14px;color:#555;padding:16px 20px;box-shadow:0 1px 4px rgba(0,0,0,.05)}
.field svg{position:absolute;right:20px;top:17px}

/* footer */
.site-footer{top:4090px;height:388px;background:var(--footer);color:var(--white)}
.foot-brand{position:absolute;left:110px;top:55px;width:190px;height:210px;display:flex;flex-direction:column;align-items:center;justify-content:center;gap:12px}
.foot-brand .dot{width:70px;height:70px;border-radius:50%;background:var(--red)}
.foot-brand span{font-family:'Marcellus',Georgia,serif;font-size:19px;color:var(--white)}
.site-footer h6{position:absolute;top:82px;font-size:16px;font-weight:700;letter-spacing:.3px}
.foot-links a{position:absolute;left:417px;font-size:14px;color:var(--white);text-decoration:none}
.foot-text{position:absolute;font-size:13.5px;line-height:26px}
.foot-social{position:absolute;top:230px;width:40px;height:40px;border-radius:50%;background:#555}
.copyright{position:absolute;top:346px;left:0;width:1200px;text-align:center;font-size:13px;color:#ddd}
</style>
</head>
<body>

<header class="site-header">
  <nav class="nav">
    <a style="left:111px">Home</a>
    <a style="left:195px">About Us</a>
    <a style="left:301px">Join Us</a>
    <a style="left:395px">Events</a>
    <a style="left:790px">Alumni</a>
  </nav>
  <div class="abs" style="left:864px;top:63px;width:1px;height:16px;background:#bbb"></div>
  <div class="brand"><div class="dot"></div><span>Brenfield Circle</span></div>
  <div class="mail-badge">
    <svg width="50" height="50" viewBox="0 0 50 50"><rect x="15" y="18" width="20" height="14" fill="none" stroke="#fff" stroke-width="1.8"/><path d="M15 18l10 8 10-8" fill="none" stroke="#fff" stroke-width="1.8"/></svg>
  </div>
  <div class="abs serif" style="left:956px;top:50px;font-size:15px;color:var(--ink)">Email Us</div>
  <div class="abs" style="left:956px;top:73px;font-size:13px;color:var(--ink)">info@brenfieldcircle.org</div>
</header>

<section class="hero">
  <div class="hero-photo" role="img" aria-label="Student at a desk taking notes while on the phone, with a red tint over the left side"></div>
  <h2 class="kicker">Welcome to</h2>
  <h2 class="name">Brenfield Circle<br>Fraternity</h2>
  <div class="btn light" style="left:111px;top:398px;width:142px;height:54px">GET STARTED</div>
  <svg class="arrow" style="left:46px" width="24" height="40" viewBox="0 0 24 40"><path d="M20 4L4 20l16 16" fill="none" stroke="#fff" stroke-width="4"/></svg>
  <svg class="arrow" style="left:1106px" width="24" height="40" viewBox="0 0 24 40"><path d="M4 4l16 16L4 36" fill="none" stroke="#fff" stroke-width="4"/></svg>
</section>

<section class="about">
  <div class="about-mark"><div class="dot"></div><span>Brenfield Circle</span></div>
  <h2 class="title" style="left:613px;top:116px">WELCOME TO BRENFIELD CIRCLE!</h2>
  <div class="rule" style="left:613px;top:166px"></div>
  <p>Brenfield Circle is the coeducational professional criminal justice fraternity at the acclaimed Marwick Vale State University in beautiful Marwick Vale, California. Student members are individuals, of varying majors, with career goals in the criminal justice system such as law enforcement, probation, corrections, security, and law. The primary objectives of the Fraternity are to assist members with occupational preparation, career selection, career acquisition and to provide a fertile environment for academic study. Brenfield Circle also supports and promotes the Department of Justice Studies, strives to improve the campus environment, and makes positive contributions to the local community. Learn more about us!</p>
  <div class="btn" style="left:613px;top:451px;width:143px;height:54px">LEARN MORE</div>
</section>

<section class="features">
  <div class="features-bg" role="img" aria-label="Graduation caps in the air under a deep red tint"></div>
  <h2 class="title" style="left:0;width:1200px;text-align:center;top:82px;color:#fff">KEY FEATURES</h2>
  <div class="rule" style="left:556px;top:141px;background:#fff"></div>

  <div class="feature" style="left:99px">
    <div class="disc"><svg width="70" height="70" viewBox="0 0 70 70" fill="none" stroke="#8a1c12" stroke-width="2"><circle cx="35" cy="22" r="8"/><path d="M20 56c0-10 7-18 15-18s15 8 15 18z"/><path d="M12 14h10v6a5 5 0 0 1-10 0z"/><path d="M17 25v8M13 33h8"/><path d="M48 14h10v6a5 5 0 0 1-10 0z"/><path d="M53 25v8M49 33h8"/></svg></div>
    <h3>Lorem ipsum dolor</h3>
    <p>Lorem ipsum dolor sit amet,<br>consectetur adipiscing elit,<br>sed do eiusmod</p>
  </div>
  <div class="feature" style="left:355px">
    <div class="disc"><svg width="70" height="70" viewBox="0 0 70 70" fill="none" stroke="#8a1c12" stroke-width="2"><path d="M18 10h26l8 8v38H18z"/><path d="M44 10v8h8"/><path d="M24 26h20M24 33h20M24 40h12"/><path d="M46 42l8 3v6c0 5-4 8-8 9-4-1-8-4-8-9v-6z"/><path d="M42 51l3 3 5-6"/></svg></div>
    <h3>Lorem ipsum dolor</h3>
    <p>Lorem ipsum dolor sit amet,<br>consectetur adipiscing elit,<br>sed do eiusmod</p>
  </div>
  <div class="feature" style="left:613px">
    <div class="disc"><svg width="76" height="70" viewBox="0 0 76 70" fill="none" stroke="#8a1c12" stroke-width="2"><path d="M8 24L38 10l30 14z"/><path d="M10 24h56v4H10z"/><path d="M16 30v22M26 30v22M36 30v22M46 30v22M56 30v22"/><path d="M8 54h60v5H8z"/></svg></div>
    <h3>Lorem ipsum dolor</h3>
    <p>Lorem ipsum dolor sit amet,<br>consectetur adipiscing elit,<br>sed do eiusmod</p>
  </div>
  <div class="feature" style="left:869px">
    <div class="disc"><svg width="70" height="70" viewBox="0 0 70 70" fill="none" stroke="#8a1c12" stroke-width="2"><path d="M35 10v42M18 18h34"/><path d="M18 18l-8 16h16zM52 18l-8 16h16z"/><path d="M10 34a8 4 0 0 0 16 0M44 34a8 4 0 0 0 16 0"/><path d="M22 56h26v5H22z"/></svg></div>
    <h3>Lorem ipsum dolor</h3>
    <p>Lorem ipsum dolor sit amet,<br>consectetur adipiscing elit,<br>sed do eiusmod</p>
  </div>
</section>

<section class="social">
  <h2 class="title" style="left:111px;top:80px">VISIT BFC ON SOCIAL MEDIA!</h2>
  <div class="rule" style="left:111px;top:128px"></div>
  <div class="social-dot" style="left:111px" aria-label="Social network link"></div>
  <div class="social-dot" style="left:226px" aria-label="Social network link"></div>
  <div class="social-dot" style="left:342px" aria-label="Social network link"></div>
  <div class="social-dot" style="left:456px" aria-label="Social network link"></div>
  <h4>Support Our BFC</h4>
  <p>Help our organization by donating today! All donations go directly to making a difference for our cause.</p>
  <div class="btn" style="left:111px;top:444px;width:146px;height:54px">DONATE NOW</div>
  <svg class="abs" style="left:292px;top:464px" width="74" height="14" viewBox="0 0 74 14" fill="none" stroke="#999" stroke-width="1.5"><path d="M24 7H2M8 1L2 7l6 6"/><path d="M48 7h22M64 1l6 6-6 6"/></svg>
  <div class="group-photo" role="img" aria-label="Group of smiling members in matching grey sweatshirts"></div>
</section>

<section class="members">
  <div class="members-photo" role="img" aria-label="Members in masks and maroon polo shirts posing together, fading into the grey background"></div>
  <h2 class="title" style="left:599px;top:70px">OUR MEMBERSHIPS</h2>
  <div class="rule" style="left:599px;top:118px"></div>
  <p>Lorem ipsum dolor sit amet, consectetur adipiscing elit, sed do eiusmod tempor incididunt ut labore et dolore magna aliqua.Ut enim ad minim veniam, quis nostrud exercitation ullamco laboris nisi</p>
  <div class="btn" style="left:599px;top:297px;width:128px;height:54px">SUBSCRIBE</div>
</section>

<section class="shop">
  <h2 class="title" style="left:0;width:1200px;text-align:center;top:80px">SALES OF ITEMS</h2>
  <div class="rule" style="left:556px;top:128px"></div>

  <div class="product" style="left:111px">
    <div class="shot"><div class="tee" role="img" aria-label="Black t-shirt with chest emblem" style="background:linear-gradient(180deg,#1c1c1c,#333)"></div></div>
    <h5>Lorem ipsum dolor</h5><div class="price">$50</div><div class="stars">★★★★★</div><div class="btn">SALE</div>
  </div>
  <div class="product" style="left:358px">
    <div class="shot"><div class="tee" role="img" aria-label="White t-shirt with chest emblem" style="background:linear-gradient(180deg,#f2f2f2,#d9d9d9)"></div></div>
    <h5>Lorem ipsum dolor</h5><div class="price">$50</div><div class="stars">★★★★★</div><div class="btn">SALE</div>
  </div>
  <div class="product" style="left:607px">
    <div class="shot"><div class="tee" role="img" aria-label="Red t-shirt with chest emblem" style="background:linear-gradient(180deg,#e0141e,#c10d17)"></div></div>
    <h5>Lorem ipsum dolor</h5><div class="price">$50</div><div class="stars">★★★★★</div><div class="btn">SALE</div>
  </div>
  <div class="product" style="left:855px">
    <div class="shot"><div class="tee" role="img" aria-label="Black t-shirt with chest emblem" style="background:linear-gradient(180deg,#1c1c1c,#333)"></div></div>
    <h5>Lorem ipsum dolor</h5><div class="price">$50</div><div class="stars">★★★★★</div><div class="btn">SALE</div>
  </div>
</section>

<section class="contact">
  <h2 class="title" style="left:0;width:1200px;text-align:center;top:70px">CONTACT US</h2>
  <div class="rule" style="left:556px;top:118px"></div>
  <div class="field" style="left:133px;top:166px;width:455px">First Name
    <svg width="12" height="14" viewBox="0 0 12 14" fill="#555"><circle cx="6" cy="4" r="3.2"/><path d="M0 14c0-4 2.5-6 6-6s6 2 6 6z"/></svg></div>
  <div class="field" style="left:603px;top:166px;width:463px">Last Name
    <svg width="12" height="14" viewBox="0 0 12 14" fill="#555"><circle cx="6" cy="4" r="3.2"/><path d="M0 14c0-4 2.5-6 6-6s6 2 6 6z"/></svg></div>
  <div class="field" style="left:133px;top:228px;width:455px">Email Address
    <svg width="14" height="12" viewBox="0 0 14 12" fill="#555"><rect y="1" width="14" height="10"/><path d="M0 1l7 5 7-5" stroke="#fff" fill="none"/></svg></div>
  <div class="field" style="left:603px;top:228px;width:463px">Phone No
    <svg width="13" height="13" viewBox="0 0 13 13" fill="#555"><path d="M3 0l2 3-1.5 1.5a8 8 0 0 0 5 5L10 8l3 2-1.5 3C6 13 0 7 0 1.5z"/></svg></div>
  <div class="field" style="left:133px;top:289px;width:933px;height:101px">Message
    <svg width="15" height="12" viewBox="0 0 15 12" fill="none" stroke="#555" stroke-width="1.4"><ellipse cx="7.5" cy="5" rx="6.5" ry="4.3"/><path d="M4 8.5L3 11.5l4-2.4"/></svg></div>
  <div class="btn" style="left:549px;top:428px;width:103px;height:54px">SUBMIT</div>
</section>

<footer class="site-footer">
  <div class="foot-brand"><div class="dot"></div><span>Brenfield Circle</span></div>
  <h6 style="left:417px">QUICK LINKS</h6>
  <div class="foot-links">
    <a style="top:132px">Home</a>
    <a style="top:158px">About Us</a>
    <a style="top:184px">Join Us</a>
    <a style="top:210px">Events</a>
  </div>
  <h6 style="left:620px">CONTACT US</h6>
  <svg class="abs" style="left:620px;top:138px" width="14" height="20" viewBox="0 0 14 20" fill="#fff"><path d="M7 0a7 7 0 0 1 7 7c0 5-7 13-7 13S0 12 0 7a7 7 0 0 1 7-7z"/><circle cx="7" cy="7" r="2.6" fill="#2b2b2b"/></svg>
  <div class="foot-text" style="left:651px;top:133px">48 Larkspur Avenue<br>Marwick Vale, California</div>
  <svg class="abs" style="left:620px;top:201px" width="16" height="12" viewBox="0 0 16 12" fill="#fff"><rect width="16" height="12"/><path d="M0 0l8 6 8-6" stroke="#2b2b2b" fill="none" stroke-width="1.4"/></svg>
  <div class="foot-text" style="left:651px;top:194px">info@brenfieldcircle.org</div>
  <h6 style="left:863px">NEWSLETTER</h6>
  <div class="abs" style="left:863px;top:132px;width:226px;height:40px;background:#fff;border-radius:3px;font-size:13px;color:#888;padding:12px 14px">Enter email</div>
  <div class="abs" style="left:1035px;top:132px;width:54px;height:40px;background:var(--red);border-radius:0 3px 3px 0">
    <svg style="position:absolute;left:19px;top:14px" width="16" height="12" viewBox="0 0 16 12" fill="#fff"><rect width="16" height="12"/><path d="M0 0l8 6 8-6" stroke="#8a1c12" fill="none" stroke-width="1.4"/></svg>
  </div>
  <div class="foot-social" style="left:883px" aria-label="Social network link"></div>
  <div class="foot-social" style="left:938px" aria-label="Social network link"></div>
  <div class="foot-social" style="left:992px" aria-label="Social network link"></div>
  <div class="foot-social" style="left:1047px" aria-label="Social network link"></div>
  <div class="copyright">©Copyrights 2023 Brenfield Circle &nbsp;&nbsp;|&nbsp;&nbsp; All Rights Reserved</div>
</footer>

</body>
</html>
```